Print on top the name of the company: (Or Similar)
Larkmoor Cleaning & Disinfecting
Because your standards aren't standard.

We adhere to ALL NVB guidelines for both residential and commercial cleaning.

Infection Control is our ultimate goal.

Instructions:
Opening a residential and commercial cleaning and disinfecting company in south Florida.

Targeting high-end residential clients, commercial and healthcare facilities, specializing in Ambulatory Care Guidelines. With a concentration and expertise in targeting Covid 19 and other transmissible pathogens.

UMRE trained.
Owned and operated by a licensed BSN Registered Nurse specially ​trained in Infection Control Prevention with over 25 years experience. Over two decades in Ambulatory Surgery Center Administration, Director of Nursing and Infection Control Prevention ad Consulting.

Looking to create a business flier that emphasizes Cleaning & Disinfection
along with the standard expectation for residential and Commercial cleaning services
Updates

Need extra days to review

Target Market(s)

Residential & Commercial

Font styles to use
Decorative

Requirements
Must have
• A checklist for cleaning services

```html
<!DOCTYPE html>
<html lang="en">
<head>
<meta charset="utf-8">
<title>Larkmoor Cleaning &amp; Disinfecting – Flyer</title>
<link href="https://fonts.googleapis.com/css2?family=Montserrat:wght@300;400;500;600;700;800&family=Oswald:wght@600;700&display=swap" rel="stylesheet">
<style>
  :root{
    --navy:#2b3766;
    --navy-deep:#232e58;
    --green:#9ac43c;
    --white:#ffffff;
    --ink:#283361;
    --backdrop:#ecebea;
    --photo-light:#a3adbb;
    --photo-mid:#56637f;
  }
  *{margin:0;padding:0;box-sizing:border-box}
  html,body{width:783px;height:1200px;overflow:hidden;background:var(--backdrop)}
  body{font-family:"Montserrat",Arial,sans-serif;color:var(--ink)}
  .canvas{position:relative;width:783px;height:1200px;overflow:hidden;background:var(--backdrop)}
  .flyer{position:absolute;left:0;top:46px;width:712px;height:1007px;transform:scale(1.0997);transform-origin:0 0;background:var(--navy);overflow:hidden}
  .flyer-shapes{position:absolute;inset:0;width:712px;height:1007px}

  .headline{position:absolute;left:312px;width:380px;text-transform:uppercase;font-weight:800;line-height:1;white-space:nowrap}
  .headline--name{top:70px;font-size:53px;color:var(--white);letter-spacing:.5px}
  .headline--accent{top:125px;font-size:53px;color:var(--green);letter-spacing:.5px}
  .headline--sub{top:186px;font-size:36px;font-weight:700;color:var(--white)}
  .rule{position:absolute;height:3px;background:var(--green)}
  .rule--hero{left:313px;top:240px;width:95px}
  .intro{position:absolute;left:313px;top:264px;width:330px;font-size:14.5px;line-height:19px;font-weight:600;color:var(--white)}

  .badge{position:absolute;left:386px;top:364px;width:180px;height:180px;border-radius:50%;background:var(--white);display:flex;align-items:center;justify-content:center}
  .badge-seal{width:166px;height:166px;border-radius:50%;background:var(--green);display:flex;align-items:center;justify-content:center}
  .badge-ring{width:146px;height:146px;border-radius:50%;border:2px solid var(--white);display:flex;flex-direction:column;align-items:center;justify-content:center;color:var(--white);font-family:"Oswald",Impact,sans-serif;text-transform:uppercase}
  .badge-label{font-size:15px;letter-spacing:2px;font-weight:600}
  .badge-years{font-size:34px;font-weight:700;line-height:1.15;letter-spacing:1px}

  .section-title{position:absolute;left:37px;top:556px;font-size:26px;color:var(--ink);white-space:nowrap;letter-spacing:.3px}
  .section-title strong{font-weight:700}
  .section-title span{font-weight:300}
  .list-heading{position:absolute;font-size:15px;font-weight:600;letter-spacing:.6px;text-transform:uppercase;color:var(--ink)}
  .list-heading--commercial{left:37px;top:595px}
  .list-heading--residential{left:254px;top:769px}
  .rule--commercial{left:37px;top:619px;width:42px;height:2px}
  .rule--residential{left:254px;top:799px;width:42px;height:2px}

  .checklist{position:absolute;list-style:none;font-size:14px;font-weight:600;color:var(--ink)}
  .checklist li{position:relative;height:23px;line-height:23px;padding-left:20px;white-space:nowrap}
  .checklist li::before{content:"";position:absolute;left:0;top:7px;width:10px;height:10px;border-radius:50%;background:var(--green)}
  .checklist li::after{content:"";position:absolute;left:3px;top:9px;width:3px;height:5px;border:solid var(--white);border-width:0 1.5px 1.5px 0;transform:rotate(45deg)}
  .checklist--c1{left:37px;top:634px}
  .checklist--c2{left:219px;top:634px}
  .checklist--r1{left:254px;top:820px}
  .checklist--r2{left:458px;top:820px}

  .illustration{position:absolute;border-radius:10px}
  .illustration--commercial{left:436px;top:560px;width:252px;height:184px;background:linear-gradient(160deg,#e3e7ee 0%,#c9d3e2 55%,#f2d58a 100%)}
  .illustration--residential{left:36px;top:740px;width:184px;height:180px;background:linear-gradient(160deg,#eef1f5 0%,#cdd7e8 55%,#f0d27a 100%)}

  .footer{position:absolute;left:0;top:944px;width:712px;height:63px;display:flex;align-items:center}
  .footer-cta{position:absolute;left:37px;top:14px;width:190px;font-size:11px;line-height:14px;font-weight:400;color:var(--green)}
  .footer-phone{position:absolute;left:234px;top:16px;font-size:22px;font-weight:600;color:var(--white);letter-spacing:.3px}
  .footer-divider{position:absolute;left:430px;top:16px;width:1px;height:30px;background:var(--white);opacity:.8}
  .footer-web{position:absolute;left:446px;top:22px;display:flex;align-items:center;gap:8px;font-size:14px;font-weight:700;color:var(--white);letter-spacing:.3px}
</style>
</head>
<body>
<div class="canvas">
  <div class="flyer">
    <svg class="flyer-shapes" viewBox="0 0 712 1007" aria-hidden="true">
      <defs>
        <linearGradient id="photoFade" x1="0" y1="0" x2="1" y2="0">
          <stop offset="0" stop-color="#a3adbb"/>
          <stop offset="0.5" stop-color="#56637f"/>
          <stop offset="1" stop-color="#2b3766"/>
        </linearGradient>
      </defs>
      <rect x="0" y="0" width="440" height="540" fill="url(#photoFade)"/>
      <path d="M0,466 C130,530 300,528 400,455 L560,430 C630,452 690,500 712,540 L712,1007 L0,1007Z" fill="#9ac43c"/>
      <path d="M0,488 C130,545 300,545 400,478 L560,455 C625,478 680,525 712,578 L712,936 L0,936Z" fill="#ffffff"/>
      <path d="M0,870 C8,915 40,936 100,936 L712,936 L712,944 L0,944Z" fill="#9ac43c"/>
      <rect x="0" y="944" width="712" height="63" fill="#2b3766"/>
      <path d="M660,944 C690,950 706,975 712,1007 L712,944Z" fill="#9ac43c"/>
    </svg>
    <div class="illustration" style="left:0;top:0;width:420px;height:470px;border-radius:0;background:transparent" role="img" aria-label="Photo of a technician in a white protective suit and mask spraying disinfectant along a building wall"></div>

    <h1 class="headline headline--name">Larkmoor</h1>
    <div class="headline headline--accent">Cleaning</div>
    <div class="headline headline--sub">&amp; Disinfecting</div>
    <div class="rule rule--hero"></div>
    <p class="intro">Owned and operated by a licensed BSN Registered Nurse specially trained in Infection Control Prevention with over 25 years experience.</p>

    <div class="badge">
      <div class="badge-seal">
        <div class="badge-ring">
          <span class="badge-label">Experience</span>
          <span class="badge-years">25 Years</span>
          <span class="badge-label">Experience</span>
        </div>
      </div>
    </div>

    <h2 class="section-title"><strong>BRIGHTWELL</strong> <span>CLEANING</span></h2>
    <h3 class="list-heading list-heading--commercial">Commercial Cleaning</h3>
    <div class="rule rule--commercial"></div>
    <ul class="checklist checklist--c1">
      <li>Janitorial</li><li>Offices</li><li>Floor maintenance</li><li>Carpet cleaning</li>
    </ul>
    <ul class="checklist checklist--c2">
      <li>Move-ins</li><li>Move-outs.</li><li>Constructions clean-ups</li><li>Estate clean-outs</li>
    </ul>
    <div class="illustration illustration--commercial" role="img" aria-label="Illustration of two cleaning workers in overalls with a vacuum and a cleaning cart"></div>

    <div class="illustration illustration--residential" role="img" aria-label="Illustration of two house cleaners with a mop, plant and floor lamp"></div>
    <h3 class="list-heading list-heading--residential">Residential Cleaning</h3>
    <div class="rule rule--residential"></div>
    <ul class="checklist checklist--r1">
      <li>House cleaning</li><li>Before and after party</li><li>Move-ins</li><li>Move-outs</li>
    </ul>
    <ul class="checklist checklist--r2">
      <li>Holiday cleaning</li><li>Seasonal cleaning</li><li>Carpet cleaning</li><li>Deodorizing and sanitizing</li>
    </ul>

    <footer class="footer">
      <p class="footer-cta">Call us to find out how you can save money this month!</p>
      <div class="footer-phone">(555) 014 27 83</div>
      <div class="footer-divider"></div>
      <div class="footer-web">
        <svg width="15" height="15" viewBox="0 0 16 16" aria-hidden="true" fill="none" stroke="#9ac43c" stroke-width="1.3">
          <circle cx="8" cy="8" r="6.8"/><ellipse cx="8" cy="8" rx="3" ry="6.8"/><line x1="1.2" y1="8" x2="14.8" y2="8"/><line x1="2.2" y1="4.5" x2="13.8" y2="4.5"/><line x1="2.2" y1="11.5" x2="13.8" y2="11.5"/>
        </svg>
        <span>www.larkmoorclean.com</span>
      </div>
    </footer>
  </div>
</div>
</body>
</html>
```